Tech House track needs a Cover design!

I need a CD Cover for an unreleased Tech House track. Please find attached a snipped of the song so you get an impression how it feels. I will also attach two existing covers which are already made for other tracks. I want to use kind of corporate design so it would be great if you design a cover which for example fits to the circle which is used in previous covers. Be creative in this. I will also provide my Logo so you can already place it on the cover. Name of the track is "Driftwood" which should also be found on the cover art.

Target Market(s)

Young people enjoying Tech House music on festivals or in a sunset session in their favourite venue.

Industry/Entity Type

Music Download

Colors

Designer to choose colors to be used in the design.

Requirements
Must have
• Circle kind of design. Including the logo and track title. Should fit electronic music!!
Nice to have
• can include kind of natural motives...maybe an implied sunset...
Should not have
• not too futuristic, no comic style,

```html
<!DOCTYPE html>
<html lang="en">
<head>
<meta charset="utf-8">
<title>Driftwood – Cover</title>
<link rel="stylesheet" href="https://fonts.googleapis.com/css2?family=Orbitron:wght@600;800&display=swap">
<style>
  :root {
    --backdrop: #7d0603;
    --ice-white: #f2f8fd;
    --ice-light: #c9e3f7;
    --ice-mid: #8cc2ea;
    --ice-deep: #4f95cf;
    --title-blue: #2c7fd0;
    --title-edge: #0f3f78;
    --figure-blue: #3f88c8;
    --figure-deep: #1d5d9c;
    --logo-blue: #2a78c8;
    --rule-blue: #2f7fc9;
  }
  * { margin: 0; padding: 0; box-sizing: border-box; }
  html, body {
    width: 1200px;
    height: 850px;
    overflow: hidden;
    background: var(--backdrop);
  }
  .cover {
    position: absolute;
    left: 240px;
    top: 65px;
    width: 720px;
    height: 720px;
    overflow: hidden;
    box-shadow: 0 14px 40px rgba(0,0,0,0.35);
  }
  .cover__pattern {
    position: absolute;
    inset: 0;
    background:
      radial-gradient(circle at 50% 52%,
        var(--ice-white) 0%,
        var(--ice-light) 22%,
        var(--ice-white) 34%,
        var(--ice-mid) 48%,
        var(--ice-light) 60%,
        var(--ice-mid) 78%,
        var(--ice-deep) 100%);
  }
  .cover__title {
    position: absolute;
    top: 82px;
    left: 0;
    width: 100%;
    text-align: center;
    font-family: "Orbitron", sans-serif;
    font-weight: 800;
    font-size: 62px;
    letter-spacing: 4px;
    color: var(--title-blue);
    text-shadow: 0 2px 0 var(--title-edge), 0 4px 8px rgba(15,63,120,0.35);
  }
  .cover__figure {
    position: absolute;
    left: 288px;
    top: 173px;
    width: 173px;
    height: 338px;
    border-radius: 80px;
    background: linear-gradient(180deg, var(--figure-blue), var(--figure-deep) 50%, var(--figure-blue));
    opacity: 0.85;
  }
  .cover__rule {
    position: absolute;
    left: 162px;
    width: 540px;
    height: 6px;
    background: var(--rule-blue);
    border-radius: 1px;
  }
  .cover__rule--top { top: 598px; }
  .cover__rule--bottom { top: 688px; }
  .cover__label {
    position: absolute;
    top: 614px;
    left: 162px;
    width: 540px;
    height: 64px;
    display: flex;
    align-items: center;
    justify-content: center;
    gap: 16px;
    font-family: "Orbitron", sans-serif;
    font-weight: 800;
    font-size: 48px;
    letter-spacing: 3px;
    color: var(--logo-blue);
  }
  .cover__label-dot {
    width: 36px;
    height: 36px;
    border-radius: 50%;
    background: var(--logo-blue);
  }
</style>
</head>
<body>
  <main class="cover">
    <div class="cover__pattern" role="img" aria-label="Radial kaleidoscope of petal shapes in icy blue and white"></div>
    <h1 class="cover__title">DRIFTWOOD</h1>
    <div class="cover__figure" role="img" aria-label="Mirrored silhouette of a human head in icy translucent blue"></div>
    <div class="cover__rule cover__rule--top"></div>
    <div class="cover__label">
      <span class="cover__label-dot"></span>
      <span class="cover__label-name">NORTHMERE</span>
    </div>
    <div class="cover__rule cover__rule--bottom"></div>
  </main>
</body>
</html>
```